Infectious Diseases Research Laboratory Needs Business Card

We need a business card for an academic research laboratory based in Kansas City called MORVEK. The full lab name is Microbial Dose-Response/Exposure Bridging Studies Laboratory, but this does not need to be incorporated. We study novel ways to optimize the treatment of multidrug-resistant bacterial infections ("superbugs") throughout the entire biomedical research spectrum (from benchtop to bedside). The name MORVEK is not only an acronym for our lab name, but also represents our desire to make discoveries and explore the unknown (the stars, if you well). It also serves as an ode to the state of Kansas motto where we are based, ad astra per aspera ("to the stars, through difficulty").

Target Market(s)

Pharmaceutical companies, researchers

Industry/Entity Type

Pharmaceutical

Contact Information for Business Card

The business card should incorporate and complement our new logo (see uploaded files). Double-sided designs are preferred. Looking for something modern, but professional.

Font styles to use
Sans Serif

Requirements
Must have
• Double-sided. One side would ideally be a solid color incorporating logo and the other should also have the logo (smaller), but incorporate staff information.
• Color codes:
• Red: #F04C51
• Blue: #3477B5
• Gray: #808285

```html
<!DOCTYPE html>
<html lang="en">
<head>
<meta charset="utf-8">
<title>MORVEK Business Card</title>
<link href="https://fonts.googleapis.com/css2?family=Source+Sans+3:wght@400;500;700&display=swap" rel="stylesheet">
<style>
  :root {
    --red: #F04C51;
    --blue: #3477B5;
    --gray: #808285;
    --white: #ffffff;
    --backdrop: #e9e9ea;
  }
  * { margin: 0; padding: 0; box-sizing: border-box; }
  html, body {
    width: 1200px;
    height: 900px;
    overflow: hidden;
    background: var(--backdrop);
    font-family: "Source Sans 3", sans-serif;
  }
  .canvas {
    position: relative;
    width: 1200px;
    height: 900px;
  }
  .card {
    position: absolute;
    left: 250px;
    width: 700px;
    height: 400px;
    overflow: hidden;
    box-shadow: 0 8px 24px rgba(0,0,0,0.18);
  }
  .card-back {
    top: 35px;
    background: var(--red);
    display: flex;
    flex-direction: column;
    align-items: center;
    justify-content: center;
  }
  .back-name {
    color: var(--white);
    font-size: 64px;
    font-weight: 500;
    letter-spacing: 6px;
    margin-top: 20px;
  }
  .back-web {
    position: absolute;
    bottom: 42px;
    left: 0;
    right: 0;
    text-align: center;
    color: var(--white);
    font-size: 15px;
    letter-spacing: 4px;
  }
  .card-front {
    top: 465px;
    background: var(--white);
  }
  .front-shapes {
    position: absolute;
    inset: 0;
  }
  .brand {
    position: absolute;
    left: 48px;
    top: 92px;
    display: flex;
    align-items: center;
    gap: 18px;
  }
  .brand-dot {
    width: 30px;
    height: 30px;
    border-radius: 50%;
    background: var(--blue);
  }
  .brand-name {
    color: var(--red);
    font-size: 58px;
    font-weight: 500;
    letter-spacing: 4px;
    line-height: 1;
  }
  .contact {
    position: absolute;
    left: 44px;
    top: 238px;
    color: var(--white);
    font-size: 18px;
    line-height: 1.2;
  }
  .contact-name { font-weight: 700; font-size: 20px; }
  .contact-title { font-size: 19px; margin-bottom: 6px; }
  .contact-line b { font-weight: 700; }
</style>
</head>
<body>
<div class="canvas">

  <section class="card card-back">
    <div class="back-name">MORVEK</div>
    <div class="back-web">www.morvek.org</div>
  </section>

  <section class="card card-front">
    <svg class="front-shapes" width="700" height="400" viewBox="0 0 700 400">
      <polygon points="0,200 700,70 700,400 0,400" fill="var(--blue)"/>
      <circle cx="630" cy="95" r="100" fill="var(--red)"/>
      <circle cx="634" cy="91" r="97" fill="var(--white)"/>
    </svg>

    <div class="brand">
      <span class="brand-dot"></span>
      <span class="brand-name">MORVEK</span>
    </div>

    <div class="contact">
      <div class="contact-name">DANA WHITLOCK</div>
      <div class="contact-title">CEO/FOUNDER</div>
      <div class="contact-line">1420 Larkspur Avenue</div>
      <div class="contact-line">Kansas City, Kansas 66112</div>
      <div class="contact-line"><b>P:</b> 555 214 7702 <b>C:</b> 555 381 0926</div>
      <div class="contact-line"><b>F:</b> 555 617 4483 <b>E:</b> dana@morvek.org</div>
    </div>
  </section>

</div>
</body>
</html>
```